Brightwall painting and decorating *

Need a flyer design to advertise my services
So the information I need included is the services we offer at brightwall painting and decorating which include
Interior painting
Exterior painting
Wallpaper hanging
Paint and cellulose spraying
Dust free sanding
Pressure washing
Stone cleaning
Also would need to have my company contact details in
Www.brightwallpaintingdecorating.co.uk
Email is info@brightwallpaintingdecorating.com
Brightwall Painting & Decorating Services has a proven track record of innovative designs, effective problem solving and attention to detail and our goal is to meet and exceed the expectations of every customer. We take on all types of jobs from small domestic work to larger commercial projects, all carried out to the highest standards, and at very competitive prices.
Colors
Designer to choose colors to be used in the design.
Look and feel

```html
<!DOCTYPE html>
<html lang="en">
<head>
<meta charset="utf-8">
<title>Brightwall Painting and Decorating – Flyer</title>
<link rel="stylesheet" href="https://fonts.googleapis.com/css2?family=Open+Sans:wght@300;400;600;700&family=Oswald:wght@600&display=swap">
<style>
  :root{
    --navy:#234a7a;
    --sky:#4a7fbd;
    --ink:#1f3f6b;
    --paper:#ffffff;
    --stage:#eceae6;
    --rule:#2d5588;
  }
  *{box-sizing:border-box;margin:0;padding:0}
  html,body{width:1200px;height:1200px;overflow:hidden;background:var(--stage)}
  body{font-family:"Open Sans",Arial,sans-serif;position:relative}
  .flyer{position:absolute;left:159px;top:30px;width:882px;height:1140px;background:var(--paper);box-shadow:0 2px 10px rgba(0,0,0,.15);overflow:hidden}
  .abs{position:absolute}

  .brand-box{left:0;top:32px;width:527px;height:155px;border:1.5px solid var(--rule);border-left:none;display:flex;flex-direction:column;align-items:center;justify-content:center}
  .brand-name{font-family:"Open Sans",Arial,sans-serif;font-weight:700;color:var(--navy);text-align:center;line-height:1}
  .brand-name .main{display:block;font-size:66px;letter-spacing:1px}
  .brand-name .sub{display:block;font-size:21px;margin-top:8px;letter-spacing:.3px}
  .brand-rule{width:440px;height:2px;background:var(--navy);margin-top:16px}

  .photo-frame{left:551px;top:22px;width:305px;height:287px;border:1.5px solid var(--rule);padding:7px}
  .photo{width:100%;height:100%}
  .photo-lounge{background:linear-gradient(180deg,#e9e6dc 0%,#d7d2c4 45%,#9c9891 70%,#c8b08a 100%)}

  .intro-box{left:0;top:194px;width:527px;height:216px;border:1.5px solid var(--rule);border-left:none}
  .intro{position:absolute;left:35px;top:34px;width:470px;font-size:16.4px;line-height:20.7px;color:var(--ink)}

  .band{left:0;top:416px;width:540px;height:232px;background:var(--navy);color:#fff;text-align:center}
  .band h2{position:absolute;left:27px;top:26px;width:436px;font-family:"Oswald",Impact,sans-serif;font-weight:600;font-size:37px;line-height:1;letter-spacing:.4px;text-align:left}
  .band .place{position:absolute;left:27px;top:72px;width:436px;font-weight:300;font-size:35px;letter-spacing:9.5px;line-height:1;text-align:left;white-space:nowrap}
  .band p{position:absolute;left:24px;top:115px;width:448px;font-size:16.4px;line-height:20.6px}

  .circle{left:477px;top:315px;width:400px;height:400px;border-radius:50%;border:4px solid var(--navy);background:#fff;padding:6px;z-index:2}
  .circle .photo{border-radius:50%;background:radial-gradient(circle at 40% 40%,#f1ece2 0%,#e0d6c3 40%,#8c8580 75%,#4c4a50 100%)}

  .services-box{left:0;top:660px;width:375px;height:409px;border:1.5px solid var(--rule);border-left:none;border-top:none}
  .services-box h3{position:absolute;left:55px;top:48px;font-weight:700;font-size:33px;letter-spacing:3.6px;color:var(--sky)}
  .service-list{position:absolute;left:55px;top:100px;list-style:none}
  .service-list li{display:flex;align-items:center;height:38.8px;font-size:21px;color:#222}
  .service-list svg{width:22px;height:22px;margin-right:15px;flex:none}

  .contact-box{left:376px;top:659px;width:493px;height:163px;border:1.5px solid var(--rule);border-bottom:none}
  .contact-bar{left:376px;top:730px;width:493px;height:80px;background:var(--navy);color:#fff;display:flex;align-items:center;padding-left:34px}
  .contact-bar .label{font-weight:400;font-size:28px;letter-spacing:.5px}
  .phone-icon{width:58px;height:58px;margin:0 14px 0 18px;flex:none}
  .contact-bar .number{font-weight:700;font-size:25px;letter-spacing:.3px}

  .photo-cornice{left:375px;top:822px;width:495px;height:244px;background:linear-gradient(160deg,#5c5c60 0%,#6d6d72 40%,#e9e7e2 55%,#f6f5f1 70%,#d9d7d2 100%)}

  .footer{left:0;top:1078px;width:882px;height:62px;background:var(--navy);color:#fff;display:flex;align-items:center;font-size:16px}
  .footer .item{display:flex;align-items:center;position:absolute}
  .footer svg{margin-right:12px;flex:none}
</style>
</head>
<body>
<main class="flyer">

  <header class="abs brand-box">
    <h1 class="brand-name"><span class="main">BRIGHTWALL</span><span class="sub">PAINTING AND DECORATING SERVICES</span></h1>
    <div class="brand-rule"></div>
  </header>

  <figure class="abs photo-frame">
    <div class="photo photo-lounge" role="img" aria-label="Photo of a bright modern lounge with grey sofas and armchairs on a wooden floor"></div>
  </figure>

  <section class="abs intro-box">
    <p class="intro">Brightwall Painting &amp; Decorating Services has a proven track record of innovative designs, effective problem solving and attention to detail and our goal is to meet and exceed the expectations of every customer. We take on all types of jobs from small domestic work to larger commercial projects, all carried out to the highest standards, and at very competitive prices.</p>
  </section>

  <section class="abs band">
    <h2>ESTABLISHED DECORATORS</h2>
    <div class="place">IN SOUTH LONDON</div>
    <p>Get in touch with our expert decorators at Brightwall Painting and Decorating Services in Bexley to give your property a makeover. Our services are available across South London.</p>
  </section>

  <figure class="abs circle">
    <div class="photo" role="img" aria-label="Photo of a decorated living room with cream sofas, patterned curtains and dark floral wallpaper"></div>
  </figure>

  <section class="abs services-box">
    <h3>OUR SERVICES</h3>
    <ul class="service-list">
      <li><svg viewBox="0 0 22 22"><rect x="1.5" y="4.5" width="16" height="16" fill="none" stroke="var(--sky)" stroke-width="2.2"/><path d="M5 11.5l4.5 4.5L20.5 2.5" fill="none" stroke="var(--sky)" stroke-width="3"/></svg>Interior painting</li>
      <li><svg viewBox="0 0 22 22"><rect x="1.5" y="4.5" width="16" height="16" fill="none" stroke="var(--sky)" stroke-width="2.2"/><path d="M5 11.5l4.5 4.5L20.5 2.5" fill="none" stroke="var(--sky)" stroke-width="3"/></svg>Exterior painting</li>
      <li><svg viewBox="0 0 22 22"><rect x="1.5" y="4.5" width="16" height="16" fill="none" stroke="var(--sky)" stroke-width="2.2"/><path d="M5 11.5l4.5 4.5L20.5 2.5" fill="none" stroke="var(--sky)" stroke-width="3"/></svg>Wallpaper hanging</li>
      <li><svg viewBox="0 0 22 22"><rect x="1.5" y="4.5" width="16" height="16" fill="none" stroke="var(--sky)" stroke-width="2.2"/><path d="M5 11.5l4.5 4.5L20.5 2.5" fill="none" stroke="var(--sky)" stroke-width="3"/></svg>Paint and cellulose spraying</li>
      <li><svg viewBox="0 0 22 22"><rect x="1.5" y="4.5" width="16" height="16" fill="none" stroke="var(--sky)" stroke-width="2.2"/><path d="M5 11.5l4.5 4.5L20.5 2.5" fill="none" stroke="var(--sky)" stroke-width="3"/></svg>Dust free sanding</li>
      <li><svg viewBox="0 0 22 22"><rect x="1.5" y="4.5" width="16" height="16" fill="none" stroke="var(--sky)" stroke-width="2.2"/><path d="M5 11.5l4.5 4.5L20.5 2.5" fill="none" stroke="var(--sky)" stroke-width="3"/></svg>Pressure washing</li>
      <li><svg viewBox="0 0 22 22"><rect x="1.5" y="4.5" width="16" height="16" fill="none" stroke="var(--sky)" stroke-width="2.2"/><path d="M5 11.5l4.5 4.5L20.5 2.5" fill="none" stroke="var(--sky)" stroke-width="3"/></svg>Stone cleaning</li>
    </ul>
  </section>

  <div class="abs contact-box"></div>
  <section class="abs contact-bar">
    <span class="label">CONTACT US</span>
    <svg class="phone-icon" viewBox="0 0 58 58">
      <circle cx="29" cy="29" r="27" fill="none" stroke="#fff" stroke-width="2.5"/>
      <path d="M15 25c0-4 6-6 14-6s14 2 14 6v3h-6v-3h-16v3h-6z" fill="#fff"/>
      <path d="M20 29h18l3 10H17z" fill="#fff"/>
      <circle cx="29" cy="33.5" r="3" fill="var(--navy)"/>
    </svg>
    <span class="number">07700 900 458</span>
  </section>

  <div class="abs photo-cornice" role="img" aria-label="Close-up photo of an ornate white plaster ceiling cornice against a grey wall"></div>

  <footer class="abs footer">
    <div class="item" style="left:76px">
      <svg width="24" height="24" viewBox="0 0 24 24" fill="none" stroke="#fff" stroke-width="1.4"><circle cx="12" cy="12" r="10.5"/><ellipse cx="12" cy="12" rx="4.5" ry="10.5"/><path d="M1.5 12h21M3.5 6.5h17M3.5 17.5h17M12 1.5v21"/></svg>
      <span>Www.brightwallpaintingdecorating.co.uk</span>
    </div>
    <div class="item" style="left:468px">
      <svg width="36" height="22" viewBox="0 0 36 22" fill="none" stroke="#fff" stroke-width="1.6"><rect x="1" y="1" width="34" height="20"/><path d="M1 1l17 12L35 1M1 21l12-10M35 21L23 11"/></svg>
      <span>info@brightwallpaintingdecorating.com</span>
    </div>
  </footer>

</main>
</body>
</html>
```